Law Firm Needs a new Website Design

We need a new website design for our law firm located in Manhattan (Law Offices of Tobias R. Venkland, PLLC).
We have an existing logo that we will to continue using, which can be found in www.VenklandLaw.example.
The Prime Counsel, Top Advocates Logo should also be reflected near the bottom of the Home page.
The website will be 6 pages.

Deliverables:
I want a
1) home page,
2) About Us/Practice Areas page,
3) attorneys,
4) News and Articles page, and
5) Contact and Directions/Privacy Policy page.

The colors of my logo should be in the website.
I also like a touch of black and red.

The website should project "excellence."
We seek to provide the highest quality legal services.
We handle estate planning, wills, trusts, planning for people with disabilities, asset protection and preservation, Medicaid planning, hospital safe discharge, nursing home placement, powers of attorney, health care proxies, living wills, guardianships, probate, estate administration and related litigation.

I would like the colors of my Logo used (including shading where appropriate).
I also want some black on the borders and/or bottom and some red touches throughout the page.

My Logo should appear everywhere that "Law Offices Of Tobias R. Venkland, PLLC" appears.
I want the badges for Prime counsel, Top Advocates, Top Legal Practices, and ZELQ on the Home page.
I do not want too much text on the home page.

We would also like the website to have coding.
The final design should also communicate quality, expertise and stability.
Great start so far by the people who submitted designs.
Thank you.

Industry/Entity Type

Law Firm

Coding

Coded - Design and coding required

Number of Pages Required

5+ page

Colors
3276b5
ec1f27
474747

Requirements
Must have
• Please use my logo each time you mention Law Offices of Tobias R. Venkland, PLLC. Please include the Primecounsel, Top Advocates, Top Legal Practices and Zelq rating Badges on the web home page. I only wish to be contacted by phone. I am not including testimonials and am only using the New York City address.
Nice to have
• Prefer illustrations to photos regarding practice areas
Should not have
• Testimonials, contact me by email, free consultation.

```html
<!DOCTYPE html>
<html lang="en">
<head>
<meta charset="utf-8">
<title>Law Offices of Tobias R. Venkland, PLLC</title>
<link rel="stylesheet" href="https://fonts.googleapis.com/css2?family=Noto+Serif:wght@400;700&family=Open+Sans:wght@400;600;700&display=swap">
<style>
:root{
  --blue:#3276b5;
  --blue-dark:#2a5f98;
  --red:#ec1f27;
  --grey:#474747;
  --text:#666666;
  --light:#eeeeee;
  --dark:#3a3331;
  --white:#ffffff;
}
*{margin:0;padding:0;box-sizing:border-box}
html,body{width:1200px;height:2217px;overflow:hidden;background:var(--white)}
body{position:relative;font-family:"Open Sans",Arial,sans-serif;color:var(--text)}
.serif{font-family:"Noto Serif",Georgia,serif}
.abs{position:absolute}

/* header */
.site-header{position:absolute;left:0;top:0;width:1200px;height:104px}
.brand{position:absolute;left:77px;top:20px;display:flex;align-items:center;gap:18px}
.brand-mark{width:52px;height:52px;background:var(--blue)}
.brand-text{font-family:"Noto Serif",Georgia,serif;color:var(--blue);line-height:1.1}
.brand-text .small{font-size:17px;display:block;text-align:center}
.brand-text .name{font-size:31px;display:block}
.brand-text .small.pllc{font-size:13px;letter-spacing:2px}
.main-nav{position:absolute;top:40px;left:615px;display:flex;gap:0}
.main-nav a{font-family:"Noto Serif",Georgia,serif;font-size:19px;color:#8a8a8a;text-decoration:none;position:absolute;white-space:nowrap}
.main-nav a.active{color:var(--blue)}

/* hero */
.hero{position:absolute;left:0;top:104px;width:1200px;height:521px;
  background:linear-gradient(180deg,#dfe4e8 0%,#c9cdd1 45%,#6f6a66 70%,#3a3634 100%)}

/* welcome */
.welcome h1{position:absolute;left:80px;top:670px;font-family:"Noto Serif",Georgia,serif;font-weight:400;font-size:36px;color:var(--blue);letter-spacing:.3px}
.welcome p{position:absolute;left:80px;top:733px;width:720px;font-size:16.3px;line-height:25px;color:var(--text)}
.btn{position:absolute;display:flex;align-items:center;justify-content:center;background:var(--red);color:var(--white);font-family:"Noto Serif",Georgia,serif;font-size:20px;border-radius:4px;text-decoration:none}
.call-circle{position:absolute;left:850px;top:675px;width:271px;height:271px;border:1.5px solid var(--blue);border-radius:50%;text-align:center}
.call-circle svg{margin-top:50px}
.call-circle .label{font-family:"Noto Serif",Georgia,serif;font-size:30px;color:var(--blue);margin-top:6px}
.call-circle .number{font-family:"Noto Serif",Georgia,serif;font-size:35px;font-weight:700;color:var(--red);margin-top:2px}

/* practice areas */
.practice{position:absolute;left:0;top:995px;width:1200px;height:490px;
  background:linear-gradient(180deg,#3b3331 0%,#3a3432 55%,#2c2d31 100%)}
.practice h2{position:absolute;top:52px;width:100%;text-align:center;font-family:"Noto Serif",Georgia,serif;font-weight:400;font-size:40px;color:var(--white)}
.area-card{position:absolute;top:118px;width:234px;height:218px;background:var(--light);border:1px solid #d8d8d8}
.area-card .thumb{height:140px;background:linear-gradient(135deg,#c9c3bb,#8d8a86)}
.area-card .title{height:78px;display:flex;align-items:center;justify-content:center;text-align:center;font-family:"Noto Serif",Georgia,serif;font-size:21px;line-height:30px;color:var(--blue);padding:0 8px}

/* attorneys */
.attorneys h2{position:absolute;top:1535px;width:1200px;text-align:center;font-family:"Noto Serif",Georgia,serif;font-weight:400;font-size:38px;color:var(--blue)}
.attorney .photo{position:absolute;width:178px;height:178px;border:1.5px solid var(--blue);padding:5px}
.attorney .photo div{width:100%;height:100%;background:linear-gradient(160deg,#7d8a99,#4c4f55)}
.attorney h3{position:absolute;font-family:"Noto Serif",Georgia,serif;font-weight:400;font-size:21px;color:var(--blue)}
.attorney p{position:absolute;width:300px;font-size:15.5px;line-height:25px;color:var(--text)}
.attorney .more{position:absolute;font-size:15px;font-weight:700;color:var(--red);text-decoration:none;display:flex;align-items:center;gap:4px}

/* ratings band */
.ratings{position:absolute;left:0;top:1855px;width:1200px;height:155px;background:var(--light)}
.rating-name{position:absolute;font-family:"Noto Serif",Georgia,serif;font-size:44px}
.rating-name.grey{color:#7a7a7a}
.rating-name.red{color:#b4202a}
.rating-badge{position:absolute;left:915px;top:30px;width:106px;height:100px;background:#1f3f78;border-radius:6px}
.red-rule{position:absolute;left:0;top:2010px;width:1200px;height:10px;background:var(--red)}

/* footer */
.site-footer{position:absolute;left:0;top:2020px;width:1200px;height:197px;background:var(--blue);color:var(--white)}
.footer-nav a{position:absolute;top:20px;font-family:"Noto Serif",Georgia,serif;font-size:18px;color:var(--white);text-decoration:none}
.social{position:absolute;top:26px;display:block;width:18px;height:18px;border-radius:50%;background:var(--white)}
.footer-rule{position:absolute;left:77px;top:63px;width:1045px;height:1px;background:rgba(255,255,255,.3)}
.contact-title{position:absolute;left:80px;top:80px;font-family:"Noto Serif",Georgia,serif;font-size:18px}
.contact-icon{position:absolute;top:115px;width:52px;height:52px;border-radius:50%;background:var(--white);display:flex;align-items:center;justify-content:center}
.contact-text{position:absolute;font-size:15.5px;line-height:23px}
.contact-text strong{font-weight:700}
</style>
</head>
<body>

<header class="site-header">
  <div class="brand">
    <div class="brand-mark"></div>
    <div class="brand-text">
      <span class="small">Law Offices of</span>
      <span class="name">Tobias R. Venkland</span>
      <span class="small pllc">PLLC</span>
    </div>
  </div>
  <nav class="main-nav">
    <a class="active" href="#" style="left:0">HOME</a>
    <a href="#" style="left:92px">ABOUT</a>
    <a href="#" style="left:191px">ATTORNEY</a>
    <a href="#" style="left:327px">NEWS</a>
    <a href="#" style="left:417px">CONTACT</a>
  </nav>
</header>

<div class="hero" role="img" aria-label="Four attorneys meeting around a glass table in a bright office"></div>

<section class="welcome">
  <h1>WELCOME TO TOBIAS R. VENKLAND</h1>
  <p>Our firm was founded in 1993 by Tobias R. Venkland, a member of the National Guild of Elder Care Counsel (NGECC) and an elder law practitioner for over 19 years.&nbsp; Our firm is uniquely positioned to provide quality legal advice and representation in regards to estate planning, wills, trusts, planning for people...</p>
  <a class="btn" href="#" style="left:77px;top:858px;width:173px;height:58px">READ MORE</a>
  <div class="call-circle">
    <svg width="52" height="52" viewBox="0 0 24 24"><path fill="#3276b5" d="M6.6 10.8c1.4 2.8 3.8 5.1 6.6 6.6l2.2-2.2c.3-.3.7-.4 1-.2 1.1.4 2.3.6 3.6.6.6 0 1 .4 1 1V20c0 .6-.4 1-1 1C10.6 21 3 13.4 3 4c0-.6.4-1 1-1h3.5c.6 0 1 .4 1 1 0 1.3.2 2.5.6 3.6.1.3 0 .7-.2 1z"/></svg>
    <div class="label">CALL US ON</div>
    <div class="number">0400 555 219</div>
  </div>
</section>

<section class="practice">
  <h2>PRACTICE AREAS</h2>
  <div class="area-card" style="left:77px"><div class="thumb" role="img" aria-label="Family reviewing documents with an advisor"></div><div class="title">Estate Planning</div></div>
  <div class="area-card" style="left:347px"><div class="thumb" role="img" aria-label="Hand signing papers beside a small model house"></div><div class="title">Probate &amp; Estate Administration</div></div>
  <div class="area-card" style="left:618px"><div class="thumb" role="img" aria-label="Hand signing a legal document with a pen"></div><div class="title">Powers of Attorney</div></div>
  <div class="area-card" style="left:888px"><div class="thumb" role="img" aria-label="Handshake over a desk with documents"></div><div class="title">Supplemental Needs Trusts</div></div>
  <a class="btn" href="#" style="left:517px;top:366px;width:163px;height:56px">VIEW ALL</a>
</section>

<section class="attorneys">
  <h2>OUR ATTORNEYS</h2>
  <article class="attorney">
    <div class="photo" style="left:77px;top:1605px"><div role="img" aria-label="Portrait of Tobias R. Venkland"></div></div>
    <h3 style="left:268px;top:1602px">Tobias R. Venkland</h3>
    <p style="left:271px;top:1636px">Tobias R. Venkland was chair of the Harbor County Bar Association pro bono Elder Law Project and the past chair of the Harbor County Bar Association Elder Law Committee.</p>
    <a class="more" href="#" style="left:271px;top:1766px">READ MORE <svg width="14" height="12" viewBox="0 0 14 12"><path d="M1 1l5 5-5 5M7 1l5 5-5 5" fill="none" stroke="#ec1f27" stroke-width="2"/></svg></a>
  </article>
  <article class="attorney">
    <div class="photo" style="left:630px;top:1605px"><div role="img" aria-label="Portrait of Marisol K. Venkland"></div></div>
    <h3 style="left:821px;top:1602px">Marisol K. Venkland</h3>
    <p style="left:824px;top:1636px">Marisol K. Venkland is a graduate of Eastbrook University and the Whitmore School of Law where she participated in the Family Law Clinic.</p>
    <a class="more" href="#" style="left:824px;top:1766px">READ MORE <svg width="14" height="12" viewBox="0 0 14 12"><path d="M1 1l5 5-5 5M7 1l5 5-5 5" fill="none" stroke="#ec1f27" stroke-width="2"/></svg></a>
  </article>
</section>

<section class="ratings">
  <div class="rating-name grey" style="left:77px;top:45px">Prime Counsel</div>
  <div class="rating-name red" style="left:465px;top:45px">Top Advocates</div>
  <div class="rating-badge" role="img" aria-label="Top Legal Practices rating badge"></div>
</section>
<div class="red-rule"></div>

<footer class="site-footer">
  <nav class="footer-nav">
    <a href="#" style="left:80px">Home</a>
    <a href="#" style="left:165px">About</a>
    <a href="#" style="left:270px">Attorneys</a>
    <a href="#" style="left:405px">News</a>
    <a href="#" style="left:504px">Contact</a>
    <a href="#" style="left:621px">Privacy Policy</a>
  </nav>
  <a class="social" href="#" style="left:1022px" aria-label="Social link"></a>
  <a class="social" href="#" style="left:1060px" aria-label="Social link"></a>
  <a class="social" href="#" style="left:1102px" aria-label="Social link"></a>
  <div class="footer-rule"></div>
  <div class="contact-title">Contact Us</div>

  <div class="contact-icon" style="left:77px">
    <svg width="20" height="22" viewBox="0 0 24 24"><path fill="#ec1f27" d="M12 2C8.1 2 5 5.1 5 9c0 5.2 7 13 7 13s7-7.8 7-13c0-3.9-3.1-7-7-7zm0 9.5A2.5 2.5 0 1 1 12 6.5a2.5 2.5 0 0 1 0 5z"/></svg>
  </div>
  <div class="contact-text" style="left:138px;top:113px">88 Larkmoor Avenue, Suite<br>1204 New York 10099</div>

  <div class="contact-icon" style="left:348px">
    <svg width="20" height="20" viewBox="0 0 24 24"><path fill="#ec1f27" d="M6.6 10.8c1.4 2.8 3.8 5.1 6.6 6.6l2.2-2.2c.3-.3.7-.4 1-.2 1.1.4 2.3.6 3.6.6.6 0 1 .4 1 1V20c0 .6-.4 1-1 1C10.6 21 3 13.4 3 4c0-.6.4-1 1-1h3.5c.6 0 1 .4 1 1 0 1.3.2 2.5.6 3.6.1.3 0 .7-.2 1z"/></svg>
  </div>
  <div class="contact-text" style="left:413px;top:130px"><strong>(555) 014-2283</strong></div>

  <div class="contact-icon" style="left:619px">
    <svg width="20" height="20" viewBox="0 0 24 24"><path fill="#ec1f27" d="M6 3h9v5H6zM4 9h16v10H4zM7 12h3v2H7zm5 0h3v2h-3zm-5 3h3v2H7zm5 0h3v2h-3z"/></svg>
  </div>
  <div class="contact-text" style="left:679px;top:130px">(555) 014-7760</div>

  <div class="contact-text" style="left:891px;top:113px">© <strong>TOBIAS R. VENKLAND</strong> -<br>2016. All Rights Reserved.</div>
</footer>

</body>
</html>
```